Town Planning business needs a design (template) for planning reports and letters

I'm looking to develop a report and a letter template. I prepare town planning reports in NSW, Australia. Fairly straight forward reports which would include figures and tables. I can provide examples of similar reports. I have a logo design which I can also provide ( I have attached one file).

Target Market(s)

Professionals, local and state governments

Industry/Entity Type

Property Development

Requirements
Must have
• Title page, contents, 3 - 4 levels of headings, tables and ability to inset figures/photos and Annexure pages at end of report
Nice to have
• Ability to include short details of project in header or footer

```html
<!DOCTYPE html>
<html lang="en">
<head>
<meta charset="utf-8">
<title>Statement of Environmental Effects – Report Template</title>
<link href="https://fonts.googleapis.com/css2?family=Open+Sans:wght@400;600;700&display=swap" rel="stylesheet">
<style>
:root{
  --blue:#1aa6e4;
  --ink:#2f2f2f;
  --muted:#6b6b6b;
  --paper:#ffffff;
  --board:#e9e9e9;
  --rule:#cfd8dc;
  --photo-dark:#3b3f44;
  --photo-mid:#8a9097;
  --photo-light:#c9ced3;
  --faint:#d6d6d6;
}
*{box-sizing:border-box;margin:0;padding:0}
html,body{width:1200px;height:3096px;overflow:hidden}
body{background:var(--board);font-family:"Open Sans",Arial,sans-serif;color:var(--ink);position:relative}
.page{position:absolute;width:544px;height:720px;background:var(--paper);box-shadow:0 2px 6px rgba(0,0,0,.12);overflow:hidden}
.col-l{left:48px}.col-r{left:616px}
.row-1{top:40px}.row-2{top:804px}.row-3{top:1568px}.row-4{top:2332px}

.brand{position:absolute;top:26px;right:28px;display:flex;align-items:center;gap:6px;font-weight:600;font-size:12px;color:var(--ink);line-height:1}
.brand-mark{width:12px;height:12px;background:var(--blue)}
.footer-bar{position:absolute;right:0;bottom:22px;width:190px;height:20px;background:var(--blue);color:#fff;font-size:8px;display:flex;align-items:center;padding-left:18px}
.frame{position:absolute;left:22px;top:58px;right:22px;bottom:54px;border:1px solid var(--blue);border-right:none;border-bottom:none}

.content{position:absolute;left:44px;right:40px;top:70px;font-size:7.5px;line-height:1.55;color:var(--muted)}
.h1{font-size:15px;font-weight:600;color:var(--ink);margin-bottom:12px;letter-spacing:.3px}
.h2{font-size:9px;font-weight:700;color:var(--ink);margin:10px 0 5px}
.content p{margin-bottom:7px}
.content ul{list-style:none;margin-bottom:8px}
.content li::before{content:"• ";color:var(--blue)}
.rule{height:1px;background:var(--blue);margin:8px 0}
.photo{background:linear-gradient(135deg,var(--photo-light),var(--photo-mid) 55%,var(--photo-dark))}
.split{display:flex;gap:14px;margin:8px 0}
.split>*{flex:1}

/* Cover */
.cover-photo{position:absolute;left:0;top:0;width:320px;height:300px;background:linear-gradient(160deg,#5c6168,#2a2d31 70%)}
.cover-block{position:absolute;left:60px;top:70px;width:210px;height:290px;background:var(--blue);opacity:.92}
.cover-date{position:absolute;right:30px;top:40px;writing-mode:vertical-rl;font-size:34px;color:var(--blue);letter-spacing:4px;font-weight:400}
.cover-address{position:absolute;left:60px;top:374px;font-size:11px;color:var(--ink)}
.cover-title{position:absolute;left:40px;top:450px;font-size:26px;line-height:1.15;font-weight:400;color:var(--ink);letter-spacing:.5px}
.cover-sub{position:absolute;left:40px;top:528px;width:280px;font-size:13px;line-height:1.35;color:var(--blue)}
.cover-line{position:absolute;left:40px;top:440px;width:300px;height:1px;background:var(--ink)}

/* TOC */
.toc-side{position:absolute;left:34px;top:90px;writing-mode:vertical-rl;transform:rotate(180deg);font-size:28px;color:var(--blue);letter-spacing:3px;height:420px;text-align:right}
.toc-box{position:absolute;left:100px;top:70px;right:30px;bottom:60px;border:1px solid var(--blue);padding:90px 30px 0 28px;font-size:10px}
.toc-item{color:var(--blue);font-weight:400;margin-top:11px}
.toc-sub{font-size:6.5px;color:var(--muted);line-height:1.5;padding-left:6px}

/* Table */
.spec{width:100%;border-collapse:collapse;font-size:7px;margin-top:10px}
.spec td{border:1px solid var(--rule);padding:4px 6px;vertical-align:top}
.spec td:first-child{width:36%}
.spec tr.head td{background:var(--blue);color:#fff;font-weight:600}

.deco{position:absolute;left:72px;top:160px;width:400px;height:400px;background:var(--faint)}
</style>
</head>
<body>

<!-- Cover -->
<section class="page col-l row-1">
  <div class="cover-photo photo" role="img" aria-label="Dark interior photograph of a building"></div>
  <div class="cover-block"></div>
  <div class="cover-date">JUNE 2023</div>
  <div class="cover-address">123, Lorem Ipsum Dolor</div>
  <div class="cover-line"></div>
  <h1 class="cover-title">STATEMENT OF<br>ENVIRONMENTAL EFFECTS</h1>
  <p class="cover-sub">Lorem ipsum dolor sit amet, consectetur adipiscing elit.</p>
</section>

<!-- Table of contents -->
<section class="page col-r row-1">
  <div class="brand"><span class="brand-mark"></span><span>Orrin Vale</span></div>
  <div class="toc-side">TABLE OF CONTENTS</div>
  <div class="toc-box">
    <div class="toc-item">1.0 INTRODUCTION</div>
    <div class="toc-item">2.0 OBJECTIVES</div>
    <div class="toc-sub">1.1 Lorem ipsum dolor sit amet, consectetur adipiscing elit.<br>1.2 Lorem ipsum dolor sit amet, consectetur.</div>
    <div class="toc-item">3.0 VALUE</div>
    <div class="toc-sub">1.1 Lorem ipsum dolor sit amet, consectetur adipiscing elit.<br>1.2 Lorem ipsum dolor sit amet, consectetur.</div>
    <div class="toc-item">4.0 SITE DESCRIPTION &amp; LOCATION</div>
    <div class="toc-sub">1.1 Lorem ipsum dolor sit amet, consectetur adipiscing elit.<br>1.2 Lorem ipsum dolor sit amet, consectetur.</div>
    <div class="toc-item">5.0 DEVELOPMENT PROPOSAL</div>
    <div class="toc-sub">1.1 Lorem ipsum dolor sit amet, consectetur adipiscing elit.<br>1.2 Lorem ipsum dolor sit amet, consectetur.</div>
    <div class="toc-item">6.0 PLANNING</div>
    <div class="toc-sub">1.1 Lorem ipsum dolor sit amet, consectetur adipiscing elit.</div>
    <div class="toc-item">7.0 CONCLUSION</div>
  </div>
  <div class="footer-bar">www.orrinvale.example</div>
</section>

<!-- 1.0 Introduction -->
<section class="page col-l row-2">
  <div class="brand"><span class="brand-mark"></span><span>Orrin Vale</span></div>
  <div class="frame"></div>
  <div class="content">
    <h2 class="h1">1.0 INTRODUCTION</h2>
    <p>Lorem ipsum dolor sit amet, consectetur adipiscing elit. Sed do eiusmod tempor incididunt ut labore et dolore magna aliqua. Ut enim ad minim veniam, quis nostrud exercitation ullamco laboris nisi ut aliquip ex ea commodo consequat. Duis aute irure dolor in reprehenderit in voluptate velit esse cillum dolore eu fugiat nulla pariatur.</p>
    <p>Excepteur sint occaecat cupidatat non proident, sunt in culpa qui officia deserunt mollit anim id est laborum. Lorem ipsum dolor sit amet, consectetur adipiscing elit, sed do eiusmod tempor incididunt ut labore.</p>
    <div class="rule"></div>
    <h3 class="h2">What is Lorem Ipsum?</h3>
    <p>Lorem Ipsum is simply dummy text of the printing and typesetting industry. Lorem Ipsum has been the industry's standard dummy text ever since the 1500s, when an unknown printer took a galley of type and scrambled it to make a type specimen book. It has survived not only five centuries, but also the leap into electronic typesetting, remaining essentially unchanged.</p>
    <ul>
      <li>Lorem ipsum dolor sit amet, consectetur adipiscing elit.</li>
      <li>Lorem ipsum dolor sit amet, consectetur adipiscing elit.</li>
      <li>Lorem ipsum dolor sit amet, consectetur.</li>
      <li>Lorem ipsum dolor sit amet, consectetur adipiscing.</li>
      <li>Lorem ipsum dolor sit amet.</li>
      <li>Lorem ipsum dolor sit amet, consectetur adipiscing elit.</li>
      <li>Lorem ipsum dolor sit amet, consectetur.</li>
    </ul>
    <p>Lorem ipsum dolor sit amet, consectetur adipiscing elit, sed do eiusmod tempor incididunt ut labore et dolore magna aliqua. Ut enim ad minim veniam, quis nostrud exercitation ullamco laboris nisi ut aliquip ex ea commodo consequat.</p>
  </div>
  <div class="footer-bar">www.orrinvale.example</div>
</section>

<!-- 2.0 Objectives -->
<section class="page col-r row-2">
  <div class="brand"><span class="brand-mark"></span><span>Orrin Vale</span></div>
  <div class="frame"></div>
  <div class="content">
    <h2 class="h1">2.0 OBJECTIVES</h2>
    <p>Lorem ipsum dolor sit amet, consectetur adipiscing elit. Sed do eiusmod tempor incididunt ut labore et dolore magna aliqua. Ut enim ad minim veniam, quis nostrud exercitation ullamco laboris nisi ut aliquip ex ea commodo consequat. Duis aute irure dolor in reprehenderit in voluptate.</p>
    <h3 class="h2">2.1 Lorem ipsum dolor sit amet</h3>
    <div class="split">
      <div class="photo" style="height:170px" role="img" aria-label="Photograph of people meeting in an office"></div>
      <div>
        <h3 class="h2" style="margin-top:0">2.1 Lorem ipsum dolor sit amet</h3>
        <p>Lorem Ipsum is simply dummy text of the printing and typesetting industry. Lorem Ipsum has been the industry's standard dummy text ever since the 1500s, when an unknown printer took a galley of type and scrambled it to make a type specimen book. It has survived five centuries.</p>
      </div>
    </div>
    <p>Lorem ipsum dolor sit amet, consectetur adipiscing elit, sed do eiusmod tempor incididunt ut labore et dolore magna aliqua. Ut enim ad minim veniam, quis nostrud exercitation ullamco laboris nisi ut aliquip ex ea commodo consequat.</p>
    <p>Duis aute irure dolor in reprehenderit in voluptate velit esse cillum dolore eu fugiat nulla pariatur. Excepteur sint occaecat cupidatat non proident, sunt in culpa qui officia deserunt mollit anim id est laborum.</p>
    <ul>
      <li>Lorem ipsum dolor sit amet, consectetur adipiscing elit.</li>
      <li>Lorem ipsum dolor sit amet, consectetur.</li>
      <li>Lorem ipsum dolor sit amet, consectetur adipiscing elit.</li>
    </ul>
  </div>
  <div class="footer-bar">www.orrinvale.example</div>
</section>

<!-- 3.0 Value -->
<section class="page col-l row-3">
  <div class="brand"><span class="brand-mark"></span><span>Orrin Vale</span></div>
  <div class="frame"></div>
  <div class="content">
    <h2 class="h1">3.0 VALUE</h2>
    <div class="photo" style="height:190px;margin-bottom:12px" role="img" aria-label="Photograph of hands reviewing documents and charts on a desk"></div>
    <h3 class="h2">Lorem ipsum dolor sit amet.</h3>
    <p>Lorem ipsum dolor sit amet, consectetur adipiscing elit. Sed do eiusmod tempor incididunt ut labore et dolore magna aliqua. Ut enim ad minim veniam, quis nostrud exercitation ullamco laboris nisi ut aliquip ex ea commodo consequat. Duis aute irure dolor in reprehenderit in voluptate velit esse cillum dolore.</p>
    <h3 class="h2">3.1 Lorem ipsum dolor sit amet.</h3>
    <p>Lorem Ipsum is simply dummy text of the printing and typesetting industry. Lorem Ipsum has been the industry's standard dummy text ever since the 1500s, when an unknown printer took a galley of type and scrambled it to make a type specimen book.</p>
    <ul>
      <li>Lorem ipsum dolor sit amet, consectetur adipiscing elit.</li>
      <li>Lorem ipsum dolor sit amet, consectetur.</li>
    </ul>
  </div>
  <div class="footer-bar">www.orrinvale.example</div>
</section>

<!-- 4.0 Site description -->
<section class="page col-r row-3">
  <div class="brand"><span class="brand-mark"></span><span>Orrin Vale</span></div>
  <div class="frame"></div>
  <div class="content">
    <h2 class="h1">4.0 SITE DESCRIPTION &amp; LOCATION</h2>
    <div class="split">
      <div>
        <h3 class="h2" style="margin-top:0">Lorem ipsum dolor sit amet,</h3>
        <p>Lorem Ipsum is simply dummy text of the printing and typesetting industry. Lorem Ipsum has been the industry's standard dummy text ever since the 1500s, when an unknown printer took a galley of type and scrambled it to make a type specimen book.</p>
      </div>
      <div class="photo" style="height:150px" role="img" aria-label="Photograph of a building under construction with scaffolding"></div>
    </div>
    <div class="split">
      <div class="photo" style="height:150px" role="img" aria-label="Photograph of a street view of the site"></div>
      <div>
        <h3 class="h2" style="margin-top:0">Lorem ipsum dolor sit amet,</h3>
        <p>Lorem Ipsum is simply dummy text of the printing and typesetting industry. Lorem Ipsum has been the industry's standard dummy text ever since the 1500s, when an unknown printer took a galley of type and scrambled it.</p>
      </div>
    </div>
    <p>Lorem ipsum dolor sit amet, consectetur adipiscing elit, sed do eiusmod tempor incididunt ut labore et dolore magna aliqua. Ut enim ad minim veniam, quis nostrud exercitation ullamco laboris nisi ut aliquip ex ea commodo consequat. Duis aute irure dolor in reprehenderit.</p>
  </div>
  <div class="footer-bar">www.orrinvale.example</div>
</section>

<!-- 5.0 Development proposal -->
<section class="page col-l row-4">
  <div class="brand"><span class="brand-mark"></span><span>Orrin Vale</span></div>
  <div class="frame"></div>
  <div class="content">
    <h2 class="h1">5.0 DEVELOPMENT PROPOSAL</h2>
    <p>Lorem ipsum dolor sit amet, consectetur adipiscing elit. Sed do eiusmod tempor incididunt ut labore et dolore magna aliqua. Ut enim ad minim veniam, quis nostrud exercitation ullamco laboris nisi ut aliquip ex ea commodo consequat.</p>
    <h3 class="h2">Lorem ipsum dolor sit amet, consectetur adipiscing elit</h3>
    <p>Lorem Ipsum is simply dummy text of the printing and typesetting industry. Lorem Ipsum has been the industry's standard dummy text ever since the 1500s, when an unknown printer took a galley of type and scrambled it to make a type specimen book.</p>
    <table class="spec">
      <tr class="head"><td>Lorem Ipsum</td><td>Lorem ipsum dolor sit amet</td></tr>
      <tr><td>Site Area</td><td>Lorem ipsum dolor sit</td></tr>
      <tr><td>Floor Space Ratio</td><td>Lorem ipsum dolor sit amet, consectetur</td></tr>
      <tr class="head"><td>Lorem Ipsum</td><td>Lorem ipsum dolor sit amet</td></tr>
      <tr><td>Height</td><td>Lorem ipsum dolor</td></tr>
      <tr><td>Setbacks</td><td>Lorem – Consectetur, Ipsum dolor<br>Lorem – Adipiscing, sit amet elit</td></tr>
      <tr><td>Landscaping</td><td>Lorem ipsum dolor sit amet</td></tr>
      <tr><td>Parking</td><td>Lorem ipsum</td></tr>
    </table>
  </div>
  <div class="footer-bar">www.orrinvale.example</div>
</section>

<!-- Back panel -->
<section class="page col-r row-4" style="background:transparent;box-shadow:none">
  <div class="deco"></div>
</section>

</body>
</html>
```